Non-Fiction Book On Creativity - Cover Design / Physical and E-Book

I am looking for designs for my first book! It's called: Patience Builds Harbors. The subtitle is: 12 Chapters About Gathering Courage, Mending Fences, And Walking A Quiet Road.
It's a series of short lessons and principals on creativity and it will be a Vellora book and a physical book.
I'm really open to any type of designs but have attached some screenshots of other book covers that have a design and style that I like.
Please let me know if you have any questions or need any more information.
Creativity / Self-Help / Personal Development

```html
<!DOCTYPE html>
<html lang="en">
<head>
<meta charset="utf-8">
<title>Patience Builds Harbors — Full Cover Wrap</title>
<link href="https://fonts.googleapis.com/css2?family=Bebas+Neue&family=Josefin+Sans:wght@200&display=swap" rel="stylesheet">
<style>
  :root {
    --paper: #ffffff;
    --ink: #111111;
    --spine: #000000;
    --swirl-red: #e0453a;
    --swirl-pink: #d8346f;
    --swirl-violet: #8a3fae;
    --swirl-olive: #8f8a45;
    --swirl-grey: #9a8f98;
    --figure-grey: #c9c9c9;
  }
  * { box-sizing: border-box; margin: 0; padding: 0; }
  html, body { width: 1200px; height: 830px; overflow: hidden; background: var(--paper); }
  .cover-wrap { position: relative; width: 1200px; height: 830px; background: var(--paper); }

  .back-cover { position: absolute; left: 34px; top: 50px; width: 486px; }
  .back-blurb {
    font-family: "Bebas Neue", sans-serif;
    font-size: 12.6px; line-height: 18.4px; color: var(--ink);
    text-align: justify; margin-bottom: 18px;
  }

  .spine { position: absolute; left: 556px; top: 0; width: 92px; height: 830px; background: var(--spine); }
  .spine-title {
    position: absolute; left: 46px; top: 258px;
    transform: translate(-50%, -50%) rotate(-90deg);
    font-family: "Bebas Neue", sans-serif; font-size: 50px; line-height: 1;
    color: var(--paper); white-space: nowrap;
  }
  .spine-author {
    position: absolute; left: 46px; top: 656px;
    transform: translate(-50%, -50%) rotate(-90deg);
    font-family: "Josefin Sans", sans-serif; font-weight: 200; font-size: 20px;
    letter-spacing: 0.75em; color: var(--paper); white-space: nowrap;
  }

  .front-art { position: absolute; left: 648px; top: 0; width: 552px; height: 640px; }

  .front-author {
    position: absolute; right: 10px; top: 24px;
    font-family: "Josefin Sans", sans-serif; font-weight: 200; font-size: 31px;
    letter-spacing: 0.62em; color: var(--paper); white-space: nowrap;
  }

  .front-title { position: absolute; right: 0; top: 350px; display: flex; flex-direction: column; align-items: flex-end; }
  .front-title span {
    display: block; background: var(--spine); color: var(--paper);
    font-family: "Bebas Neue", sans-serif; font-size: 92px; line-height: 90px;
    padding: 2px 14px 0 18px; height: 90px;
  }

  .front-subtitle {
    position: absolute; right: 8px; top: 628px; text-align: right;
    font-family: "Bebas Neue", sans-serif; font-size: 32px; line-height: 40px; color: var(--ink);
  }
</style>
</head>
<body>
<main class="cover-wrap">
  <section class="back-cover">
    <p class="back-blurb">Lorem ipsum dolor sit amet, consectetur adipiscing elit. Pellentesque dui elit, tempus nec posuere eu, congue eget est. Vestibulum sagittis arcu sapien, vitae pellentesque nibh aliquam non. Sed lacinia arcu vel erat aliquam, at blandit nulla ornare. Sed sed fringilla ante, sit amet porta quam. Vestibulum ullamcorper felis nec mauris laoreet, ac tempus felis porttitor. Aenean malesuada eget tellus nec gravida. Curabitur euismod leo at ante eleifend, sed consequat turpis ornare. Aenean consectetur non risus et eleifend. Vivamus ut dignissim ante.</p>
    <p class="back-blurb">Aliquam suscipit ultrices magna sed tempor. Duis facilisis leo turpis, eu scelerisque justo imperdiet id. Vivamus mollis nunc eros, ac dictum arcu vestibulum at. Donec vitae erat ac leo porta hendrerit vel venenatis orci. Nam ullamcorper, odio at porta molestie, justo mauris imperdiet sapien, ut scelerisque arcu libero non massa. In placerat ipsum sit amet elit volutpat rhoncus. Suspendisse hendrerit nisl porttitor dui consequat, at scelerisque odio imperdiet. Integer feugiat libero id tristique vulputate. Praesent sit amet egestas mi. Phasellus finibus nibh at ante ornare, et dapibus erat rutrum. Nullam lectus risus, vestibulum laoreet vestibulum in, ullamcorper nec arcu. Nunc convallis venenatis elit semper volutpat. Integer mollis risus nec leo malesuada sodales. Pellentesque ipsum urna, rutrum sit amet nisi ac, egestas porttitor velit. Morbi leo velit, egestas id interdum a, consectetur at nisi. Sed id tellus vel mauris placerat volutpat.</p>
  </section>

  <aside class="spine">
    <div class="spine-title">Patience Builds Harbors</div>
    <div class="spine-author">Author Name</div>
  </aside>

  <section class="front-cover">
    <svg class="front-art" viewBox="648 0 552 640" width="552" height="640">
      <defs>
        <linearGradient id="swirl-paint" x1="0" y1="1" x2="1" y2="0">
          <stop offset="0" stop-color="var(--swirl-olive)"/>
          <stop offset="0.35" stop-color="var(--swirl-red)"/>
          <stop offset="0.6" stop-color="var(--swirl-grey)"/>
          <stop offset="0.8" stop-color="var(--swirl-pink)"/>
          <stop offset="1" stop-color="var(--swirl-violet)"/>
        </linearGradient>
        <linearGradient id="figure-tone" x1="0" y1="0" x2="0" y2="1">
          <stop offset="0" stop-color="#d6d6d6"/>
          <stop offset="1" stop-color="var(--figure-grey)"/>
        </linearGradient>
      </defs>
      <path role="img" aria-label="Swirling painted canvas in red, pink, violet and olive tones"
            fill="url(#swirl-paint)"
            d="M836,0 C800,50 760,95 752,150 L756,420 C790,430 840,440 866,440 C866,400 900,362 960,352 L1200,352 L1200,0 Z"/>
      <rect role="img" aria-label="Pencil sketch of a painter at an easel holding a palette"
            x="684" y="150" width="190" height="478" rx="40" fill="url(#figure-tone)" opacity="0.55"/>
    </svg>

    <div class="front-author">Author Name</div>

    <h1 class="front-title">
      <span>Patience</span>
      <span>Builds</span>
      <span>Harbors</span>
    </h1>

    <p class="front-subtitle">12 Chapters About Gathering Courage,<br>Mending Fences, And Walking A Quiet Road.</p>
  </section>
</main>
</body>
</html>
```